Corporate Business Card

Very professional, Modern, Not to busy, include phone address email, website
(541) 555-0174, 61807 19th Street N, Avon, OR 98517, marcus@kestrelbayholding.com, brelvanindustries.com

Target Market(s)

Manufacturing

Industry/Entity Type

Aero, machining, manufacturing, Off road racing

Contact Information for Business Card

Phone, address email, website

```html
<!DOCTYPE html>
<html lang="en">
<head>
<meta charset="utf-8">
<title>Brelvan Industries – Business Card</title>
<link href="https://fonts.googleapis.com/css2?family=Lato:wght@400;700;900&display=swap" rel="stylesheet">
<style>
  :root {
    --navy: #163369;
    --red: #d6262e;
    --muted: #5a6690;
    --paper: #ffffff;
    --backdrop: #e6e6e6;
  }
  * { margin: 0; padding: 0; box-sizing: border-box; }
  html, body {
    width: 1200px;
    height: 801px;
    overflow: hidden;
    background: var(--backdrop);
    font-family: "Lato", Arial, sans-serif;
  }
  .card {
    position: absolute;
    left: 352px;
    width: 521px;
    height: 298px;
    overflow: hidden;
  }
  .card--front { top: 45px; background: var(--paper); }
  .card--back { top: 424px; background: var(--navy); }

  .brand {
    position: absolute;
    display: flex;
    align-items: center;
    gap: 8px;
    font-weight: 900;
    font-size: 22px;
    letter-spacing: 0.04em;
    white-space: nowrap;
  }
  .brand__mark { width: 12px; height: 12px; background: var(--red); }
  .card--front .brand { top: 34px; right: 26px; color: var(--navy); }
  .card--back .brand { bottom: 28px; right: 24px; color: #ffffff; }

  .person {
    position: absolute;
    top: 134px;
    left: 0;
    padding-left: 17px;
    border-left: 12px solid var(--red);
  }
  .person__name {
    font-weight: 700;
    font-size: 20px;
    line-height: 20px;
    color: var(--navy);
    margin-left: -12px;
    padding-left: 4px;
  }
  .person__role {
    font-size: 13.5px;
    color: var(--muted);
    margin-left: -12px;
    padding-left: 4px;
    margin-top: 2px;
  }

  .contact {
    position: absolute;
    left: 282px;
    top: 180px;
    list-style: none;
  }
  .contact__item {
    display: flex;
    align-items: center;
    gap: 7px;
    font-weight: 700;
    font-size: 13.5px;
    color: var(--navy);
    height: 22px;
    white-space: nowrap;
  }
  .contact__item--address { margin-bottom: 16px; }
  .contact__icon { width: 12px; height: 12px; fill: var(--red); flex: none; }
</style>
</head>
<body>
  <section class="card card--front">
    <div class="brand"><span class="brand__mark"></span>BRELVAN INDUSTRIES</div>

    <div class="person">
      <div class="person__name">DANIEL HARLOW</div>
      <div class="person__role">founder &amp; CEO</div>
    </div>

    <ul class="contact">
      <li class="contact__item contact__item--address">
        <svg class="contact__icon" viewBox="0 0 12 12" aria-hidden="true"><path d="M6 0a4.3 4.3 0 0 0-4.3 4.3C1.7 7.5 6 12 6 12s4.3-4.5 4.3-7.7A4.3 4.3 0 0 0 6 0zm0 6a1.7 1.7 0 1 1 0-3.4A1.7 1.7 0 0 1 6 6z"/></svg>
        19th Street N, Avon, OR 98517
      </li>
      <li class="contact__item">
        <svg class="contact__icon" viewBox="0 0 12 12" aria-hidden="true"><path d="M6 0a6 6 0 1 0 0 12A6 6 0 0 0 6 0zm4.6 5.3H8.7a9 9 0 0 0-.8-3.6 4.8 4.8 0 0 1 2.7 3.6zM6 1.2c.6.8 1.3 2.3 1.4 4.1H4.6C4.7 3.5 5.4 2 6 1.2zM4.1 1.7a9 9 0 0 0-.8 3.6H1.4a4.8 4.8 0 0 1 2.7-3.6zM1.4 6.7h1.9a9 9 0 0 0 .8 3.6 4.8 4.8 0 0 1-2.7-3.6zM6 10.8c-.6-.8-1.3-2.3-1.4-4.1h2.8C7.3 8.5 6.6 10 6 10.8zm1.9-.5a9 9 0 0 0 .8-3.6h1.9a4.8 4.8 0 0 1-2.7 3.6z"/></svg>
        brelvanindustries.com
      </li>
      <li class="contact__item">
        <svg class="contact__icon" viewBox="0 0 12 12" aria-hidden="true"><path d="M2.4.5 4.3 2.6c.3.3.3.8 0 1.1l-.9.9a7.6 7.6 0 0 0 4 4l.9-.9c.3-.3.8-.3 1.1 0l2.1 1.9c.3.3.3.8 0 1.1l-1 1C9.3 12.9 0 8.4.3 2.4l1-1.9c.3-.3.8-.3 1.1 0z"/></svg>
        (541) 555-0174, 61807
      </li>
      <li class="contact__item">
        <svg class="contact__icon" viewBox="0 0 12 12" aria-hidden="true"><path d="M0 2.5h12v.6L6 6.8 0 3.1z"/><path d="M0 4.3l6 3.7 6-3.7V10H0z"/></svg>
        marcus@kestrelbayholding.com
      </li>
    </ul>
  </section>

  <section class="card card--back">
    <div class="brand"><span class="brand__mark"></span>BRELVAN INDUSTRIES</div>
  </section>
</body>
</html>
```